Quillory Points website re-design and

the institute of massage therapy is ready for a new website. The current website is around 12 years old and it looks old. Luckily the clients is not against changing the colors so the new design does not have to use the current ugly green color scheme. Be creative! Make it pretty, modern and inviting. The current colors look like mold. Nobody likes mold. I have attached the logo asset file as well as a txt document that details the new website design parameters

1 page

```html
<!DOCTYPE html>
<html lang="en">
<head>
<meta charset="utf-8">
<title>Institute of Calmwater Therapy — Massage Continuing Education</title>
<link rel="stylesheet" href="https://fonts.googleapis.com/css2?family=Cormorant+Garamond:wght@400;500&family=Great+Vibes&family=Inter:wght@400;500;600&display=swap">
<style>
:root{
  --gold:#c4a66a;
  --gold-dark:#b39455;
  --ink:#1f1f1f;
  --text:#333333;
  --muted:#6b6b6b;
  --line:#9a9a9a;
  --paper:#ffffff;
  --footer:#2a2928;
  --serif:"Cormorant Garamond", Georgia, serif;
  --sans:"Inter", Arial, sans-serif;
  --script:"Great Vibes", cursive;
}
*{box-sizing:border-box;margin:0;padding:0}
html,body{width:1200px;height:4458px;overflow:hidden}
body{position:relative;background:var(--paper);font-family:var(--sans);color:var(--text)}
.abs{position:absolute}
.btn{position:absolute;display:flex;align-items:center;justify-content:center;font-family:var(--sans);font-weight:600;letter-spacing:2.4px;text-transform:uppercase;font-size:11.5px}
.btn-dark{background:var(--ink);color:#fff}
.btn-gold{background:var(--gold);color:#fff}
.photo{position:absolute}

/* header */
.site-header{position:absolute;left:0;top:0;width:1200px;height:99px;background:#fff}
.brand{position:absolute;display:flex;align-items:center;gap:10px;font-family:var(--sans);font-weight:500;letter-spacing:1.5px;text-transform:uppercase;color:var(--ink)}
.brand-dot{width:18px;height:18px;border-radius:50%;background:var(--ink)}
.main-nav a{position:absolute;top:44px;font-size:14px;font-weight:500;color:var(--ink);text-decoration:none}
.main-nav a.active::after{content:"";position:absolute;left:-6px;right:-6px;bottom:-10px;height:2px;background:var(--gold)}

/* hero */
.hero{position:absolute;left:0;top:99px;width:1200px;height:573px;background:linear-gradient(100deg,#6b5a4f 0%,#9a8374 35%,#c8b4a3 60%,#e8ddd3 80%,#b28a7e 100%)}
.hero-kicker{position:absolute;left:156px;top:118px;font-family:var(--script);font-size:34px;color:#fff}
.hero-title{position:absolute;left:156px;top:170px;font-family:var(--serif);font-weight:400;font-size:50px;line-height:58px;color:#fff}
.hero-copy{position:absolute;left:156px;top:310px;width:400px;font-size:13.5px;line-height:25px;color:#fff}
.field{position:absolute;top:406px;height:41px;background:#fff;border:1px solid #ddd;font-size:11px;color:#666;display:flex;align-items:center;padding:0 11px}

/* packages */
.section-title{position:absolute;left:0;width:1200px;text-align:center;font-family:var(--serif);font-weight:400;font-size:42px;color:var(--ink)}
.rule{position:absolute;height:1px;background:var(--line)}
.center-copy{position:absolute;left:0;width:1200px;text-align:center;font-size:13.5px;line-height:25px;color:var(--text)}
.package{position:absolute;top:940px;width:280px;height:298px}
.package-name{position:absolute;left:0;top:155px;width:100%;text-align:center;font-family:var(--serif);font-size:27px;line-height:29px;color:#fff}
.package .btn{left:64px;top:232px;width:152px;height:42px}
.pager{position:absolute;top:1270px;width:38px;height:38px;border-radius:50%}

/* certification */
.cert-band{position:absolute;left:0;top:1351px;width:1200px;height:707px;background:linear-gradient(110deg,#2a140b 0%,#7a3f1c 35%,#a9622b 50%,#5a2b14 75%,#2b130a 100%)}
.card{position:absolute;background:#fff}
.cert-sheet{position:absolute;left:38px;top:38px;right:38px;bottom:38px;background:#efe9df;border:3px solid #c9c3b8}
.cert-seal{position:absolute;right:26%;bottom:16%;width:34px;height:34px;border-radius:50%;background:var(--gold)}
.cert-heading{position:absolute;left:26px;top:36px;font-family:var(--serif);font-size:36px;line-height:42px;color:var(--ink)}

/* about */
.about-title{position:absolute;left:156px;top:2182px;font-family:var(--serif);font-size:42px;color:var(--ink)}
.about-copy{position:absolute;left:156px;top:2248px;width:356px;font-size:13.5px;line-height:25px;color:var(--text)}

/* banners */
.band-title{position:absolute;left:0;width:100%;text-align:center;font-family:var(--serif);font-size:42px;color:#fff}
.band-copy{position:absolute;left:0;width:100%;text-align:center;font-size:13.5px;line-height:25px;color:#fff}

/* footer */
.site-footer{position:absolute;left:0;top:3989px;width:1200px;height:469px;background:var(--footer)}
.social{position:absolute;top:4163px;width:20px;height:20px;border-radius:50%;background:#fff}
.foot-nav a{position:absolute;top:4312px;font-size:13.5px;font-weight:500;color:#fff;text-decoration:none}
</style>
</head>
<body>

<header class="site-header">
  <div class="brand" style="left:52px;top:36px;font-size:17px"><span class="brand-dot"></span>Institute of Calmwater Therapy</div>
  <nav class="main-nav">
    <a class="active" href="#" style="left:461px">Home</a>
    <a href="#" style="left:536px">Courses</a>
    <a href="#" style="left:626px">Guidelines</a>
    <a href="#" style="left:734px">Faqs</a>
    <a href="#" style="left:801px">Policies</a>
    <a href="#" style="left:888px">Contact</a>
    <a href="#" style="left:978px">About</a>
  </nav>
  <svg class="abs" style="left:1060px;top:36px" width="32" height="30" viewBox="0 0 32 30" fill="none" stroke="#1f1f1f" stroke-width="2">
    <path d="M2 4h5l4 15h14l3-10H9"/><circle cx="13" cy="25" r="2"/><circle cx="23" cy="25" r="2"/>
  </svg>
  <div class="abs" style="left:1080px;top:30px;width:16px;height:16px;border-radius:50%;background:var(--gold);color:#fff;font-size:10px;display:flex;align-items:center;justify-content:center">0</div>
  <svg class="abs" style="left:1121px;top:39px" width="26" height="26" viewBox="0 0 26 26" fill="none" stroke="#1f1f1f" stroke-width="2.2">
    <circle cx="11" cy="11" r="8"/><path d="M17 17l7 7"/>
  </svg>
</header>

<section class="hero" role="img" aria-label="Woman resting on a massage table wrapped in a white towel, with pink orchids in the foreground">
  <p class="hero-kicker">Welcome to our</p>
  <h1 class="hero-title">Massage Continuing<br>Education Center</h1>
  <p class="hero-copy">Committed to Excellence in Massage Therapy Continuing Education. Essentially it's an online school for massage continuing education.</p>
  <div class="field" style="left:156px;width:185px">Search by Keyword</div>
  <div class="field" style="left:353px;width:184px;justify-content:space-between">Number of CE Hours
    <svg width="12" height="8" viewBox="0 0 12 8" fill="none" stroke="#222" stroke-width="1.8"><path d="M1 1l5 5 5-5"/></svg>
  </div>
  <div class="btn btn-dark" style="left:547px;top:406px;width:151px;height:41px;font-size:13px">Search</div>
</section>

<section>
  <h2 class="section-title" style="top:740px">Our Packages</h2>
  <div class="rule" style="left:395px;top:814px;width:172px"></div>
  <div class="rule" style="left:635px;top:814px;width:172px"></div>
  <p class="center-copy" style="top:849px">Committed to Excellence in Massage Therapy Continuing Education.<br>Essentially it's an online school for massage continuing education.</p>

  <article class="package" style="left:156px">
    <div class="photo" role="img" aria-label="Therapist's hands massaging a client's lower back" style="inset:0;background:linear-gradient(160deg,#8a6b59,#c79e84 50%,#6e5547)"></div>
    <h3 class="package-name">New York<br>Package</h3>
    <div class="btn btn-gold">View Details</div>
  </article>
  <article class="package" style="left:459px">
    <div class="photo" role="img" aria-label="Woman with long hair in soft grey light" style="inset:0;background:linear-gradient(160deg,#9b9693,#c7c1bb 50%,#8a817a)"></div>
    <h3 class="package-name">Maryland<br>Package</h3>
    <div class="btn btn-gold">View Details</div>
  </article>
  <article class="package" style="left:764px">
    <div class="photo" role="img" aria-label="Client receiving a facial massage" style="inset:0;background:linear-gradient(160deg,#b98d6f,#dcb596 50%,#8f6a53)"></div>
    <h3 class="package-name">Customize Your<br>Own Package</h3>
    <div class="btn btn-gold">View Details</div>
  </article>

  <div class="pager" style="left:558px;border:1.5px solid #333;display:flex;align-items:center;justify-content:center">
    <svg width="10" height="14" viewBox="0 0 10 14" fill="none" stroke="#333" stroke-width="2"><path d="M8 1L2 7l6 6"/></svg>
  </div>
  <div class="pager" style="left:603px;background:var(--gold);display:flex;align-items:center;justify-content:center">
    <svg width="10" height="14" viewBox="0 0 10 14" fill="none" stroke="#fff" stroke-width="2"><path d="M2 1l6 6-6 6"/></svg>
  </div>
</section>

<section class="cert-band" role="img" aria-label="Woman relaxing on a massage table in warm candlelight">
  <div class="card" style="left:537px;top:107px;width:239px;height:231px">
    <h2 class="cert-heading">Our<br>Certification</h2>
    <div class="btn btn-dark" style="left:26px;top:140px;width:186px;height:40px;font-size:11px">View Certificates</div>
  </div>
  <div class="card" style="left:804px;top:80px;width:240px;height:230px"><div class="cert-sheet"><span class="cert-seal"></span></div></div>
  <div class="card" style="left:537px;top:367px;width:239px;height:230px"><div class="cert-sheet"><span class="cert-seal"></span></div></div>
  <div class="card" style="left:804px;top:339px;width:240px;height:231px"><div class="cert-sheet"><span class="cert-seal"></span></div></div>
  <div class="abs" style="left:937px;top:547px;width:210px;height:42px;background:var(--gold);color:#fff;font-family:var(--serif);font-size:18px;display:flex;align-items:center;justify-content:center">Certified Massage Doula</div>
  <div class="btn btn-gold" style="left:937px;top:597px;width:107px;height:27px;font-size:9px;letter-spacing:1.5px">View Details</div>
</section>

<section>
  <h2 class="about-title">About Us</h2>
  <div class="rule" style="left:551px;top:2208px;width:45px;background:var(--gold)"></div>
  <p class="about-copy">The Institute of Calmwater Therapy is committed to providing the best online home study continuing education courses available to massage therapists. Institute of Calmwater Therapy is approved by the National Council for Bodywork Standards (NCBS) as a continuing education Approved Provider.</p>
  <div class="btn btn-dark" style="left:156px;top:2447px;width:175px;height:44px;font-size:11px">More About Us</div>
  <div class="photo" role="img" aria-label="Woman receiving a shoulder massage" style="left:611px;top:2110px;width:329px;height:376px;background:linear-gradient(150deg,#7a4a2a,#c58a5c 55%,#e0b48a)"></div>
  <div class="photo" role="img" aria-label="Open hands holding a white flower" style="left:816px;top:2357px;width:228px;height:220px;background:linear-gradient(150deg,#c9d3d6,#e8ecec 55%,#b9c3c6)"></div>
</section>

<section class="abs" style="left:54px;top:2659px;width:1093px;height:393px;background:linear-gradient(100deg,#3d2a22,#7e5a48 40%,#a88169 65%,#c9a68f)" role="img" aria-label="Therapist massaging the shoulders of a relaxed woman, with an orchid and candle">
  <h2 class="band-title" style="top:114px">Take A Free Course</h2>
  <p class="band-copy" style="top:175px">Click here to get started today &amp; try our FREE online course!</p>
  <div class="btn btn-gold" style="left:459px;top:227px;width:175px;height:43px;font-size:11px">Try It Now</div>
</section>

<section>
  <div class="abs" style="left:156px;top:3131px;width:280px;height:442px;background:var(--gold)"></div>
  <h2 class="abs" style="left:192px;top:3186px;font-family:var(--serif);font-weight:400;font-size:42px;line-height:48px;color:#fff">Our Popular<br>Courses</h2>
  <div class="btn btn-dark" style="left:192px;top:3282px;width:208px;height:40px;font-size:11px">Shop Our Courses</div>
  <p class="abs" style="left:513px;top:3212px;width:530px;font-size:13.5px;line-height:25px">Our massage therapy continuing education courses are valid for most state massage therapy CEU requirements. See our State Guidelines page for specific information about the continuing education laws in your state.</p>
  <div class="photo" role="img" aria-label="Woman receiving a back massage" style="left:192px;top:3370px;width:269px;height:155px;background:linear-gradient(150deg,#d9c4b4,#b88a6c 50%,#efe4dc)"></div>
  <div class="photo" role="img" aria-label="Pregnant belly held in hands" style="left:485px;top:3370px;width:268px;height:155px;background:linear-gradient(150deg,#c79a9c,#e2bcbd 50%,#b28587)">
    <p class="abs" style="left:0;top:62px;width:100%;text-align:center;font-family:var(--serif);font-size:26px;color:#fff">Pregnancy / Doula</p>
  </div>
  <div class="photo" role="img" aria-label="Woman applying oil in a bright room" style="left:776px;top:3370px;width:268px;height:155px;background:linear-gradient(150deg,#efe6de,#c9a48a 55%,#f3ece6)"></div>
  <div class="abs" style="left:1055px;top:3428px;width:38px;height:38px;border-radius:50%;background:#111;display:flex;align-items:center;justify-content:center">
    <svg width="10" height="14" viewBox="0 0 10 14" fill="none" stroke="#fff" stroke-width="2"><path d="M2 1l6 6-6 6"/></svg>
  </div>
</section>

<section class="abs" style="left:0;top:3655px;width:1200px;height:334px;background:linear-gradient(100deg,#4a2c14,#8a5a30 30%,#3c2514 60%,#1e150f)" role="img" aria-label="Candles and spa stones on a wooden surface">
  <h2 class="band-title" style="top:70px">Join The Calmwater Therapy Over Now</h2>
  <p class="band-copy" style="top:130px">This community is here to encourage and support you in having open and honest conversations about<br>money so you can stop spinning your wheels and finally gain clarity and confidence with your finances.</p>
  <div class="btn btn-gold" style="left:513px;top:211px;width:175px;height:41px;font-size:11px">Click To Join</div>
</section>

<footer class="site-footer">
  <div class="brand" style="left:0;width:1200px;justify-content:center;top:102px;font-size:20px;color:#fff"><span class="brand-dot" style="background:#fff;width:22px;height:22px"></span>Institute of Calmwater Therapy</div>
</footer>
<span class="social" style="left:518px"></span>
<span class="social" style="left:563px"></span>
<span class="social" style="left:609px"></span>
<span class="social" style="left:654px"></span>
<div class="abs" style="left:333px;top:4223px;width:389px;height:43px;border:1px solid #fff;border-right:none;background:#2a2928;color:#fff;font-size:13px;display:flex;align-items:center;padding-left:16px">Get In Touch</div>
<div class="btn" style="left:722px;top:4223px;width:144px;height:43px;background:#fff;color:var(--ink);font-size:11px">Sign In</div>
<nav class="foot-nav">
  <a href="#" style="left:279px">Home</a>
  <a href="#" style="left:367px">Courses</a>
  <a href="#" style="left:472px">Guidelines</a>
  <a href="#" style="left:593px">Faqs</a>
  <a href="#" style="left:673px">Policies</a>
  <a href="#" style="left:774px">Contact</a>
  <a href="#" style="left:877px">About</a>
</nav>
<div class="rule" style="left:0;top:4399px;width:1200px;background:#555"></div>
<p class="abs" style="left:0;top:4422px;width:1200px;text-align:center;font-size:13.5px;color:#fff">Copyright © Institute Of Calmwater Therapy &nbsp;2022 &nbsp;| &nbsp;All Rights Reserved</p>

</body>
</html>
```